Business Consulting Business Card

professional business card with basic information (1) First and Last name (2) email address, (3) phone number, (4) website.

```html
<!DOCTYPE html>
<html lang="en">
<head>
<meta charset="UTF-8">
<title>Tide Harbor Business Card</title>
<link href="https://fonts.googleapis.com/css2?family=Montserrat:wght@400;500;600&display=swap" rel="stylesheet">
<style>
  :root {
    --page-bg: #e9e6e1;
    --card-white: #ffffff;
    --teal: #5fb8ad;
    --teal-blue: #3d8fa8;
    --ink: #1f3340;
    --navy-top: #0f4c5e;
    --navy-bottom: #05263b;
    --ring-light: #62a8b8;
    --text-light: #ffffff;
  }
  * { box-sizing: border-box; margin: 0; padding: 0; }
  html, body { width: 1200px; height: 859px; overflow: hidden; }
  body {
    background: var(--page-bg);
    font-family: "Montserrat", sans-serif;
    position: relative;
  }
  .card {
    position: absolute;
    top: 288px;
    width: 502px;
    height: 285px;
    overflow: hidden;
    box-shadow: 0 6px 16px rgba(0,0,0,0.18);
  }
  .card-front { left: 59px; background: var(--card-white); }
  .card-back {
    left: 639px;
    background: linear-gradient(135deg, var(--navy-top) 0%, var(--navy-bottom) 100%);
  }

  .brand {
    position: absolute;
    left: 24px;
    top: 32px;
    display: flex;
    align-items: center;
    gap: 14px;
  }
  .brand-dot {
    width: 30px; height: 30px;
    border-radius: 50%;
    background: var(--teal);
  }
  .brand-name {
    font-size: 18px;
    font-weight: 500;
    letter-spacing: 4px;
    color: var(--ink);
  }

  .person { position: absolute; left: 24px; top: 124px; }
  .person-name {
    font-size: 17px;
    font-weight: 600;
    color: var(--teal-blue);
    letter-spacing: 0.3px;
    line-height: 1.1;
  }
  .person-title {
    font-size: 12.5px;
    color: var(--ink);
    line-height: 1.3;
  }
  .divider {
    position: absolute;
    left: 24px; top: 177px;
    width: 151px; height: 1px;
    background: var(--teal-blue);
  }

  .contacts {
    position: absolute;
    left: 24px; top: 198px;
    list-style: none;
  }
  .contacts li {
    display: flex;
    align-items: center;
    gap: 6px;
    height: 17px;
    font-size: 13px;
    color: var(--ink);
  }
  .contacts svg { width: 12px; height: 12px; flex: none; }
  .web-strong { color: var(--teal-blue); font-weight: 600; }

  .front-accent {
    position: absolute;
    left: 295px; top: 102px;
    width: 208px; height: 208px;
    border-radius: 50%;
    background: var(--teal);
  }
  .back-accent {
    position: absolute;
    left: 19px; top: -9px;
    width: 172px; height: 172px;
    border-radius: 50%;
    border: 30px solid var(--ring-light);
  }
  .back-name {
    position: absolute;
    left: 0; right: 0;
    top: 200px;
    text-align: center;
    font-size: 37px;
    font-weight: 400;
    letter-spacing: 9px;
    color: var(--text-light);
    padding-left: 90px;
  }
</style>
</head>
<body>
  <section class="card card-front">
    <div class="brand">
      <span class="brand-dot"></span>
      <span class="brand-name">TIDE HARBOR</span>
    </div>

    <div class="person">
      <p class="person-name">MARCUS ELLERY</p>
      <p class="person-title">Managing Broker</p>
    </div>
    <div class="divider"></div>

    <ul class="contacts">
      <li>
        <svg viewBox="0 0 12 12" fill="none" stroke="#3d8fa8" stroke-width="1.1"><circle cx="6" cy="6" r="5.2"/><path d="M4 3.5l1 1.3-.6.7c.4.9 1.1 1.6 2 2l.7-.6 1.3 1-.6.9c-2 0-4.4-2.4-4.4-4.4z"/></svg>
        (305) 555-0148
      </li>
      <li>
        <svg viewBox="0 0 12 12" fill="none" stroke="#3d8fa8" stroke-width="1.1"><rect x="0.8" y="2.3" width="10.4" height="7.4"/><path d="M0.8 2.5L6 6.8l5.2-4.3"/></svg>
        info@tideharbor.com
      </li>
      <li>
        <svg viewBox="0 0 12 12" fill="none" stroke="#3d8fa8" stroke-width="1"><circle cx="6" cy="6" r="5.2"/><ellipse cx="6" cy="6" rx="2.3" ry="5.2"/><path d="M0.8 6h10.4M1.6 3.4h8.8M1.6 8.6h8.8"/></svg>
        <span>www.<span class="web-strong">tideharbor</span>.com</span>
      </li>
    </ul>

    <div class="front-accent"></div>
  </section>

  <section class="card card-back">
    <div class="back-accent"></div>
    <p class="back-name">TIDE HARBOR</p>
  </section>
</body>
</html>
```